VELORA5 SPORTS NETWORK

design a website that will be a companion to a sports network that features womens sports and fitness content.
With the goal of promoting and empowering female athleticism, Velora5tv.example will be the online network that connects female sports fans to the sports they love and follow. The site aims to raise the level of awareness of women in sports by providing comprehensive sports coverage, spotlighting outstanding achievements, and working with sporting associations on advocacy issues and empowering programs.
Updates
I would like to have all entry by Sunday June 8 2014 thank you
please use actual script not lorem ipsum
thank you
Deadline winding down, added new pictures to file
Target Market(s)
our target market is females 18-54, whom love womens sports and ftiness
Industry/Entity Type
Fitness
Font styles to use
Requirements
Must have
- Attributes of the website:
1. Large Photos: to accompany current stories
2. Colorful: Highlight Velora5’s officials colors
3. News Area: recent news items on the home page and achieved news stories
4. Featured Content area: Headline news, athlete spotlights and issues
5. Streaming content: to accompany news and featured content
6. Advertiser links: to purchase merchandise
7. Real-time scores of live events
8. Blog
9. Monthly newsletter
10. Athlete profile page
11. Model close to QRTV
Nice to have
- Velora5tv.example will offer value-added service that will entitle customers to gain access to online streaming services provided by Velora5, which delivers both live streams and on-demand replays of global women’s sports events to sports fans in U.S. and abroad. This service will be subscription based for a modest monthly fee. Content will be available across multiple platforms and cloud based. New subscriber will get first 30 days free.
Content will include:
1. Live sports events
2. On-demand and premium content
3. Fan-generated Content

```html
<!DOCTYPE html>
<html lang="en">
<head>
<meta charset="utf-8">
<title>Velora5 Sports Network</title>
<link rel="stylesheet" href="https://fonts.googleapis.com/css2?family=Oswald:wght@400;500&family=Open+Sans:wght@400;600;700&family=PT+Sans+Narrow:wght@400;700&display=swap">
<style>
:root{
  --red:#e5252b;
  --red-bright:#f03c2f;
  --red-deep:#d81f28;
  --charcoal:#3a393e;
  --ink:#2b2a30;
  --paper:#ffffff;
  --mist:#f3f3f3;
  --button-grey:#d9d9d9;
  --salmon:#e9a394;
}
*{box-sizing:border-box;margin:0;padding:0}
html,body{width:1200px;height:2618px;overflow:hidden;background:var(--paper)}
body{font-family:"Open Sans",Arial,sans-serif;color:var(--ink)}
.page{position:relative;width:1200px;height:2618px;overflow:hidden}
.abs{position:absolute}
.narrow{font-family:"PT Sans Narrow","Arial Narrow",sans-serif}
.heading{font-family:"Oswald","Arial Narrow",sans-serif;font-weight:400}
.media{position:absolute;display:block}

/* top bar */
.top-bar{left:0;top:0;width:1200px;height:43px;background:linear-gradient(#3c3b40,#1f1e22)}
.top-bar .account{right:68px;top:10px;color:#e6e6e6;font-size:17px;font-weight:700;letter-spacing:.3px}

/* header */
.site-header{left:0;top:43px;width:1200px;height:96px;background:var(--paper)}
.brand{left:70px;top:22px;display:flex;align-items:center;gap:8px}
.brand-mark{width:14px;height:14px;border-radius:50%;background:var(--red)}
.brand-name{font-family:"PT Sans Narrow",sans-serif;font-weight:700;font-size:24px;color:var(--red)}
.main-nav a{position:absolute;top:37px;color:var(--red);font-weight:700;font-size:19px;text-decoration:none;font-family:"PT Sans Narrow",sans-serif;letter-spacing:.3px}
.stream-button{left:954px;top:19px;width:209px;height:58px;background:var(--button-grey);display:flex;align-items:center;justify-content:center;gap:14px;color:var(--red);font-size:21px;font-weight:700}

/* hero */
.hero-photo{left:0;top:139px;width:918px;height:641px;background:radial-gradient(ellipse at 28% 45%,#c9a79a 0%,#d8d2ce 35%,#ecebea 70%,#e4e3e2 100%)}
.hero-title{right:336px;top:248px;color:var(--red);font-family:"Open Sans",sans-serif;font-weight:700;font-size:37px;letter-spacing:-.5px;white-space:nowrap}
.hero-sub{right:338px;top:306px;text-align:right;color:var(--red);font-weight:700;font-size:31px;line-height:38px}
.slider-strip{left:473px;top:715px;width:445px;height:65px;background:linear-gradient(90deg,rgba(60,60,64,0),rgba(60,60,64,.75) 20%,rgba(60,60,64,.75) 80%,rgba(60,60,64,0))}
.slider-dots{left:604px;top:732px;display:flex;gap:17px}
.slider-dots span{width:29px;height:29px;border-radius:50%;background:#f2f2f2}
.slider-dots span.active{background:var(--red)}

.live-panel{left:918px;top:139px;width:282px;height:373px;background:linear-gradient(160deg,var(--red-deep),var(--red-bright))}
.live-panel h2{position:absolute;left:28px;top:20px;color:#fff;font-size:24px;font-weight:700}
.live-card{position:absolute;left:32px;width:205px;height:100px;background:linear-gradient(135deg,#6f7c96,#b5886f 55%,#4c5770)}
.live-card p{position:absolute;left:0;bottom:0;width:100%;height:26px;background:rgba(40,40,46,.85);color:#fff;font-size:16px;font-weight:700;text-align:center;line-height:26px;white-space:nowrap}
.live-panel .see-all{position:absolute;left:36px;top:315px;color:#fff;font-size:19px;font-weight:700}

.trial-panel{left:918px;top:512px;width:282px;height:268px;background:var(--charcoal)}
.trial-panel h2{position:absolute;right:27px;top:67px;text-align:right;color:#fff;font-size:22px;font-weight:700;line-height:29px;letter-spacing:.3px}
.trial-button{position:absolute;left:54px;top:147px;width:208px;height:50px;background:var(--paper);color:var(--ink);font-size:21px;font-weight:700;display:flex;align-items:center;justify-content:center}

/* scores */
.scores-bar{left:0;top:780px;width:1200px;height:47px;background:var(--charcoal)}
.scores-bar span{position:absolute;top:10px;color:#fff;font-size:20px;font-weight:400}

/* news */
.news{left:0;top:827px;width:1200px;height:442px;background:var(--mist)}
.section-title{position:absolute;font-size:39px;line-height:1}
.news .section-title{left:71px;top:20px;color:var(--ink)}
.news-item{position:absolute;left:97px;width:900px}
.news-photo{left:0;top:0;width:203px;height:153px;background:linear-gradient(135deg,#5f6b4c,#b7876e 50%,#3d4a36)}
.news-item h3{position:absolute;left:220px;top:8px;font-size:33px;font-weight:600;color:var(--ink);white-space:nowrap}
.news-item p{position:absolute;left:220px;top:63px;font-size:20px;line-height:29px;color:var(--ink);width:700px}

/* blog */
.blog{left:0;top:1269px;width:1200px;height:431px;background:linear-gradient(90deg,var(--red-deep),var(--red-bright))}
.blog .section-title{left:73px;top:42px;color:#fff}
.blog-board{position:absolute;left:68px;top:107px;width:1035px;height:272px;background:var(--mist)}
.blog-card{position:absolute;top:19px;text-align:right}
.blog-photo{left:0;top:0;height:124px}
.blog-card h4{position:absolute;right:0;top:143px;white-space:nowrap;color:var(--red);font-size:17px;font-weight:700}
.blog-card p{position:absolute;right:0;top:168px;white-space:nowrap;font-size:16px;line-height:23px;color:var(--ink)}
.blog-card time{position:absolute;right:0;top:213px;white-space:nowrap;font-size:21px;color:var(--ink)}

/* merchandise */
.merch{left:0;top:1700px;width:1200px;height:309px;background:var(--paper);border-left:3px solid var(--red);border-top:2px solid #f0b9b5}
.merch .section-title{left:63px;top:17px;color:var(--red-deep)}
.product{position:absolute;top:77px;width:140px;height:210px}
.product-shape{top:0;height:136px;left:50%;transform:translateX(-50%)}
.product .price{position:absolute;top:159px;left:0;width:140px;text-align:center;color:var(--red);font-family:"PT Sans Narrow",sans-serif;font-weight:700;font-size:27px;line-height:25px}

/* testimonials */
.testimonials{left:0;top:2009px;width:1200px;height:325px;background:linear-gradient(100deg,#e8b7a4,var(--salmon) 40%,#de8e80 75%,#c98070)}
.testimonials h2{position:absolute;left:0;width:1200px;top:66px;text-align:center;font-size:70px;line-height:1.2;color:var(--ink);font-family:"Oswald",sans-serif;font-weight:400}
.testimonials p{position:absolute;left:100px;width:1000px;top:174px;text-align:center;font-family:"PT Sans Narrow",sans-serif;font-size:23px;line-height:29px;color:var(--ink)}

/* footer */
.site-footer{left:0;top:2334px;width:1200px;height:284px;background:var(--red)}
.footer-col{position:absolute;top:60px;text-align:right;font-family:"PT Sans Narrow",sans-serif;color:#fff}
.footer-col h5{font-size:21px;font-weight:400;margin-bottom:6px;white-space:nowrap}
.footer-col li{list-style:none;font-size:16px;line-height:31px;white-space:nowrap}
.newsletter{position:absolute;left:753px;top:64px}
.newsletter h5{font-family:"Oswald",sans-serif;font-weight:400;font-size:30px;color:#fff;line-height:1}
.newsletter-form{position:absolute;left:0;top:36px;display:flex}
.newsletter-form .field{width:219px;height:37px;background:#fff;font-family:"PT Sans Narrow",sans-serif;font-size:21px;font-weight:700;color:var(--red);padding:5px 6px}
.newsletter-form .submit{width:114px;height:37px;background:var(--ink);color:#fff;font-size:20px;font-weight:600;display:flex;align-items:center;justify-content:center}
.social{position:absolute;left:921px;top:2503px;display:flex;gap:5px}
.social span{width:29px;height:29px;border-radius:50%;background:#fff}
.copyright{position:absolute;left:0;width:1200px;top:2583px;text-align:center;font-family:"PT Sans Narrow",sans-serif;font-size:18px;color:#fff}
</style>
</head>
<body>
<div class="page">

  <div class="abs top-bar"><span class="abs account narrow">REGISTER | LOG IN</span></div>

  <header class="abs site-header">
    <div class="abs brand"><span class="brand-mark"></span><span class="brand-name">VELORA5</span></div>
    <nav class="main-nav">
      <a style="left:238px" href="#">ABOUT</a>
      <a style="left:379px" href="#">BLOG</a>
      <a style="left:510px" href="#">MERCHANDISE</a>
    </nav>
    <div class="abs stream-button narrow">STREAMING LIVE
      <svg width="26" height="30" viewBox="0 0 26 30"><path d="M3 3 L23 15 L3 27 Z" fill="none" stroke="#e5252b" stroke-width="4" stroke-linejoin="round"/></svg>
    </div>
  </header>

  <section class="hero">
    <div class="media hero-photo" role="img" aria-label="Female athlete in a black training top and red shorts, seen from behind"></div>
    <h1 class="abs hero-title">WELCOME TO VELORA5</h1>
    <p class="abs hero-sub">ONLINE STREAMING<br>SERVICES</p>
    <div class="abs slider-strip"></div>
    <div class="abs slider-dots"><span class="active"></span><span></span><span></span><span></span></div>

    <aside class="abs live-panel">
      <h2 class="narrow">STREAMING LIVE</h2>
      <div class="live-card" style="top:73px" role="img" aria-label="Runners crossing a finish line"><p class="narrow">WOMEN'S 5000M FINAL</p></div>
      <div class="live-card" style="top:200px" role="img" aria-label="Sprinters racing on a track"><p class="narrow">4X100M RELAY HEATS</p></div>
      <span class="see-all narrow">See All</span>
    </aside>

    <aside class="abs trial-panel">
      <h2 class="narrow">ONLINE STREAMING<br>SERVICES</h2>
      <div class="trial-button narrow">Free 30 days trial</div>
    </aside>
  </section>

  <div class="abs scores-bar narrow">
    <span style="left:79px">Real-time scores of live events</span>
    <span style="left:469px">Real-time scores of live events</span>
    <span style="left:804px">Real-time scores of live events</span>
  </div>

  <section class="abs news">
    <h2 class="section-title heading">NEWS</h2>
    <article class="news-item" style="top:73px">
      <div class="media news-photo" role="img" aria-label="Runners celebrating at the finish of a race"></div>
      <h3>RECORD SET IN 10K</h3>
      <p>A LATE SURGE ON THE FINAL LAP DELIVERED A NEW SEASON BEST<br>AND A PLACE IN THIS SUMMER'S CHAMPIONSHIP FINAL</p>
    </article>
    <article class="news-item" style="top:261px">
      <div class="media news-photo" role="img" aria-label="Distance runner leading a pack on the track"></div>
      <h3>ATHLETE SPOTLIGHT</h3>
      <p>HOW ONE DISTANCE RUNNER BALANCES COACHING, STUDY AND<br>TRAINING WHILE CHASING HER FIRST NATIONAL TITLE</p>
    </article>
  </section>

  <section class="abs blog">
    <h2 class="section-title heading">BLOG</h2>
    <div class="blog-board">
      <article class="blog-card" style="left:23px;width:179px">
        <div class="media blog-photo" style="width:179px;background:linear-gradient(135deg,#c9c2bb,#b5675a 50%,#6d7a8e)" role="img" aria-label="Marathon runners on a road"></div>
        <h4>MARATHON PREP</h4><p>Build your long run<br>one week at a time</p><time>Jun 1, 2014</time>
      </article>
      <article class="blog-card" style="left:295px;width:195px">
        <div class="media blog-photo" style="width:195px;background:linear-gradient(135deg,#dce8ef,#c8a58f 45%,#8fb55a)" role="img" aria-label="Women jogging together in a park"></div>
        <h4>RUN TOGETHER</h4><p>Why training partners<br>keep you on track</p><time>Jun 1, 2014</time>
      </article>
      <article class="blog-card" style="left:568px;width:185px">
        <div class="media blog-photo" style="width:185px;background:linear-gradient(90deg,#e0748a,#ecd46a 50%,#a8c46e)" role="img" aria-label="Fruit smoothies against a blue sky"></div>
        <h4>FUEL UP RIGHT</h4><p>Three smoothies for<br>faster recovery</p><time>Jun 1, 2014</time>
      </article>
      <article class="blog-card" style="left:819px;width:178px">
        <div class="media blog-photo" style="width:178px;background:linear-gradient(135deg,#c9c2bb,#b5675a 50%,#6d7a8e)" role="img" aria-label="Marathon runners on a road"></div>
        <h4>RACE DAY TIPS</h4><p>Pacing advice from<br>elite road runners</p><time>Jun 1, 2014</time>
      </article>
    </div>
  </section>

  <section class="abs merch">
    <h2 class="section-title heading">MERCHANDISE</h2>
    <div class="product" style="left:71px"><div class="media product-shape" style="width:112px;background:linear-gradient(135deg,#e0386a,#c8285a 70%,#5d6fc0)" role="img" aria-label="Pink running shorts"></div><p class="price">Shorts<br>$79</p></div>
    <div class="product" style="left:220px"><div class="media product-shape" style="width:110px;background:linear-gradient(135deg,#d8307a,#b01f60)" role="img" aria-label="Pink long-sleeve training top"></div><p class="price">Top<br>$79</p></div>
    <div class="product" style="left:369px"><div class="media product-shape" style="width:58px;background:linear-gradient(90deg,#1d1d22,#2c2c33 70%,#d8306a)" role="img" aria-label="Black running tights with pink trim"></div><p class="price">Tights<br>$79</p></div>
    <div class="product" style="left:518px"><div class="media product-shape" style="width:86px;background:linear-gradient(135deg,#2a2a30,#151518)" role="img" aria-label="Black long-sleeve base layer"></div><p class="price">Base<br>$79</p></div>
    <div class="product" style="left:667px"><div class="media product-shape" style="width:112px;background:linear-gradient(135deg,#e0386a,#c8285a 70%,#5d6fc0)" role="img" aria-label="Pink running shorts"></div><p class="price">Shorts<br>$79</p></div>
    <div class="product" style="left:816px"><div class="media product-shape" style="width:110px;background:linear-gradient(135deg,#d8307a,#b01f60)" role="img" aria-label="Pink long-sleeve training top"></div><p class="price">Top<br>$79</p></div>
    <div class="product" style="left:965px"><div class="media product-shape" style="width:58px;background:linear-gradient(90deg,#1d1d22,#2c2c33 70%,#d8306a)" role="img" aria-label="Black running tights with pink trim"></div><p class="price">Tights<br>$79</p></div>
  </section>

  <section class="abs testimonials" role="img" aria-label="Woman stretching on the floor in running shoes, under a warm red tint">
    <h2>Testimonials</h2>
    <p>"Finally one place where I can follow every women's race live and catch the replays later.<br>The athlete stories keep me motivated to train, and the free trial sold me in a week." &ndash; Dana, Ohio</p>
  </section>

  <footer class="abs site-footer">
    <div class="footer-col" style="right:1008px"><h5>Navigation</h5><ul><li>Home</li><li>About Us</li><li>Our Products</li><li>Contact Us</li></ul></div>
    <div class="footer-col" style="right:810px"><h5>Product Info</h5><ul><li>Apparel</li><li>Footwear</li><li>Gear</li><li>Gift Cards</li></ul></div>
    <div class="footer-col" style="right:610px"><h5>Useful Info</h5><ul><li>Privacy Policy</li><li>Terms &amp; Agreement</li><li>FAQ</li><li>SiteMap</li></ul></div>
    <div class="newsletter">
      <h5>Monthly Newsletter</h5>
      <div class="newsletter-form"><span class="field">Enter e-mail</span><span class="submit">Subscribe</span></div>
    </div>
  </footer>
  <div class="social" aria-label="Social links"><span></span><span></span><span></span><span></span><span></span></div>
  <p class="copyright">CopyRight 2014 Velora5tv.example</p>

</div>
</body>
</html>
```